Harbor Thinktank (WordPress Hosting)

The site I would like is a robust message board. Each forum will be a group of people discussing and tracking their goals. I would also like areas
on the site for advertisers. Something similar to https://uprising.gymquokka.example/

Coding

Coded - Design and coding required

Number of Pages Required

1 page

Requirements
Must have
• Message Board

```html
<!DOCTYPE html>
<html lang="en">
<head>
<meta charset="utf-8">
<title>Iron Summit — Recent Forums</title>
<link rel="stylesheet" href="https://fonts.googleapis.com/css2?family=Montserrat:wght@400;500&family=Open+Sans:wght@400&display=swap">
<style>
:root{
  --orange:#ef5a22;
  --green:#7cbc2b;
  --ink:#2b2b2b;
  --muted:#555;
  --page:#f3f3f3;
  --white:#fff;
  --night:#050505;
  --hero-dark:#1d252c;
  --hero-mid:#4a5560;
}
*{box-sizing:border-box;margin:0;padding:0}
html,body{width:1200px;height:2739px;overflow:hidden}
body{position:relative;background:var(--page);font-family:"Open Sans",sans-serif;color:var(--ink)}
.site-header{position:absolute;top:0;left:0;width:1200px;height:94px;background:var(--white);z-index:3}
.brand{position:absolute;left:168px;top:0;width:260px;height:138px;background:var(--white);z-index:4;
  clip-path:polygon(0 0,100% 0,100% 68%,88% 100%,0 100%);display:flex;align-items:center;justify-content:center;padding-right:40px}
.site-header + .brand-cover{}
.brand-name{font-family:"Montserrat",sans-serif;font-weight:500;font-size:26px;color:var(--orange);letter-spacing:0.5px}
.brand-left{position:absolute;left:0;top:94px;width:168px;height:44px;background:var(--white);z-index:2}
.main-nav{position:absolute;top:0;left:478px;display:flex;gap:0;font-family:"Montserrat",sans-serif;font-size:15px}
.main-nav a{display:block;height:94px;line-height:96px;color:var(--ink);text-decoration:none;margin-right:35px;position:relative}
.main-nav a.is-active{color:var(--orange)}
.main-nav a.is-active::before{content:"";position:absolute;left:0;right:0;top:0;height:3px;background:var(--orange)}
.search{position:absolute;left:992px;top:38px}
.hero{position:absolute;top:94px;left:0;width:1200px;height:438px;
  background:radial-gradient(ellipse at 55% 45%,var(--hero-mid) 0%,var(--hero-dark) 60%,#11161b 100%)}
.hero-cut{position:absolute;left:920px;top:493px;width:280px;height:39px;background:var(--page);clip-path:polygon(40px 0,100% 0,100% 100%,0 100%)}
.hero-text{position:absolute;top:250px;left:0;width:1200px;text-align:center;color:var(--white);font-family:"Montserrat",sans-serif}
.hero-title{font-size:40px;font-weight:500;letter-spacing:0.3px}
.hero-rule{width:240px;height:2px;background:var(--orange);margin:8px auto 12px}
.hero-sub{font-size:22px;font-weight:400;margin-left:-36px}
.section-title{position:absolute;top:570px;left:162px;font-family:"Montserrat",sans-serif;font-weight:400;font-size:25px;color:var(--ink)}
.board{position:absolute;left:161px;width:877px;background:var(--white);box-shadow:0 1px 3px rgba(0,0,0,.12)}
.board-head{height:55px;background:var(--orange);color:var(--white);font-family:"Montserrat",sans-serif;font-size:18px;
  display:flex;align-items:center;justify-content:space-between;padding:0 22px 0 26px}
.board-body{padding-top:14px}
.topic{height:85px;display:flex;align-items:center;position:relative}
.topic-icon{position:absolute;left:23px;top:10px;width:64px;height:64px;border-radius:50%;background:var(--green)}
.topic-main{position:absolute;left:102px;top:16px}
.topic-name{font-family:"Montserrat",sans-serif;font-size:18px;color:#333}
.topic-desc{font-size:14.5px;color:var(--muted);margin-top:2px}
.topic-count{position:absolute;left:545px;top:18px;font-family:"Montserrat",sans-serif;font-size:18px;color:#444;line-height:1}
.topic-count small{display:block;font-family:"Open Sans",sans-serif;font-size:13.5px;color:var(--muted);margin-top:3px}
.topic-avatar{position:absolute;left:650px;top:17px;width:50px;height:50px;border-radius:50%;background:linear-gradient(160deg,#8a7466,#3d3a3a)}
.topic-meta{position:absolute;left:711px;top:16px;font-size:12.5px;line-height:17px;color:var(--muted)}
.topic-meta .latest{color:var(--orange)}
.more{position:absolute;top:2240px;left:573px}
.ads{position:absolute;top:2334px;left:0;width:1200px}
.ad{position:absolute;top:0}
.site-footer{position:absolute;top:2586px;left:0;width:1200px;height:153px;background:var(--night);color:var(--white)}
.footer-brand{position:absolute;left:168px;top:54px;font-family:"Montserrat",sans-serif;font-weight:500;font-size:20px}
.footer-nav{position:absolute;left:356px;top:50px;display:flex;font-family:"Montserrat",sans-serif;font-size:14px}
.footer-nav a{color:var(--white);text-decoration:none;margin-right:31px}
.copyright{position:absolute;left:356px;top:83px;font-size:12.5px;color:#bbb}
.social{position:absolute;left:916px;top:50px;display:flex;gap:34px}
.social span{width:20px;height:20px;border:2px solid var(--white);border-radius:50%}
</style>
</head>
<body>
<header class="site-header">
  <nav class="main-nav">
    <a class="is-active" href="#">ABOUT US</a>
    <a href="#">FORUMS</a>
    <a href="#">GOALS</a>
    <a href="#">HEALTH</a>
    <a href="#">CONTACT</a>
  </nav>
  <svg class="search" width="20" height="20" viewBox="0 0 20 20" aria-label="Search"><circle cx="8" cy="8" r="6" fill="none" stroke="#999" stroke-width="2.5"/><line x1="12.5" y1="12.5" x2="18" y2="18" stroke="#999" stroke-width="3"/></svg>
</header>
<div class="brand-left"></div>
<div class="brand"><span class="brand-name">IRON SUMMIT</span></div>

<section class="hero" role="img" aria-label="Helmeted warrior in a dark rainstorm"></section>
<div class="hero-cut"></div>
<div class="hero-text">
  <h1 class="hero-title">WELCOMET TO IRON SUMMIT</h1>
  <div class="hero-rule"></div>
  <p class="hero-sub">VIVAMUS PORTTITOR PURUS NISI</p>
</div>

<h2 class="section-title">RECENT FORUMS</h2>

<svg width="0" height="0" style="position:absolute">
  <defs>
    <g id="chat"><path d="M22 24c-7 0-12 4-12 9 0 3 2 5 4 6l-2 5 6-3c1 0 3 1 4 1 7 0 12-4 12-9s-5-9-12-9z" fill="none" stroke="#fff" stroke-width="2"/><path d="M30 20c7 0 12 4 12 9 0 3-2 5-4 6l2 5-6-3" fill="none" stroke="#fff" stroke-width="2"/></g>
    <g id="chev"><polyline points="2,2 14,14 26,2" fill="none" stroke="#fff" stroke-width="2.5"/></g>
  </defs>
</svg>

<section class="board" style="top:631px">
  <div class="board-head">GENERAL FITNESS <svg width="28" height="16"><use href="#chev"/></svg></div>
  <div class="board-body">
    <div class="topic"><svg class="topic-icon" viewBox="0 0 64 64"><use href="#chat"/></svg><div class="topic-main"><div class="topic-name">Fitness Training Questions</div><div class="topic-desc">Vivamus porttitor purus nisi eleifend libero a tempus libero</div></div><div class="topic-count">1200<small>Posts</small></div><div class="topic-avatar" role="img" aria-label="Member avatar"></div><div class="topic-meta"><div class="latest">Pellentesque faucibus</div><div>By Author Name</div><div>Sunday at 11:28 AM</div></div></div>
    <div class="topic"><svg class="topic-icon" viewBox="0 0 64 64"><use href="#chat"/></svg><div class="topic-main"><div class="topic-name">Weight Loss</div><div class="topic-desc">Vivamus porttitor purus nisi eleifend libero a tempus libero</div></div><div class="topic-count">525<small>Posts</small></div><div class="topic-avatar" role="img" aria-label="Member avatar"></div><div class="topic-meta"><div class="latest">Pellentesque faucibus</div><div>By Author Name</div><div>Sunday at 11:28 AM</div></div></div>
    <div class="topic"><svg class="topic-icon" viewBox="0 0 64 64"><use href="#chat"/></svg><div class="topic-main"><div class="topic-name">Achieve Goals</div><div class="topic-desc">Vivamus porttitor purus nisi eleifend libero a tempus libero</div></div><div class="topic-count">850<small>Posts</small></div><div class="topic-avatar" role="img" aria-label="Member avatar"></div><div class="topic-meta"><div class="latest">Pellentesque faucibus</div><div>By Author Name</div><div>Sunday at 11:28 AM</div></div></div>
    <div class="topic"><svg class="topic-icon" viewBox="0 0 64 64"><use href="#chat"/></svg><div class="topic-main"><div class="topic-name">Tracking Goals</div><div class="topic-desc">Vivamus porttitor purus nisi eleifend libero a tempus libero</div></div><div class="topic-count">750<small>Posts</small></div><div class="topic-avatar" role="img" aria-label="Member avatar"></div><div class="topic-meta"><div class="latest">Pellentesque faucibus</div><div>By Author Name</div><div>Sunday at 11:28 AM</div></div></div>
    <div style="height:24px"></div>
  </div>
</section>

<section class="board" style="top:1094px">
  <div class="board-head">FITNESS SPECIALITIES <svg width="28" height="16"><use href="#chev"/></svg></div>
  <div class="board-body">
    <div class="topic"><svg class="topic-icon" viewBox="0 0 64 64"><use href="#chat"/></svg><div class="topic-main"><div class="topic-name">Fitness Training Questions</div><div class="topic-desc">Vivamus porttitor purus nisi eleifend libero a tempus libero</div></div><div class="topic-count">1100<small>Posts</small></div><div class="topic-avatar" role="img" aria-label="Member avatar"></div><div class="topic-meta"><div class="latest">Pellentesque faucibus</div><div>By Author Name</div><div>Sunday at 11:28 AM</div></div></div>
    <div class="topic"><svg class="topic-icon" viewBox="0 0 64 64"><use href="#chat"/></svg><div class="topic-main"><div class="topic-name">Weight Loss</div><div class="topic-desc">Vivamus porttitor purus nisi eleifend libero a tempus libero</div></div><div class="topic-count">2200<small>Posts</small></div><div class="topic-avatar" role="img" aria-label="Member avatar"></div><div class="topic-meta"><div class="latest">Pellentesque faucibus</div><div>By Author Name</div><div>Sunday at 11:28 AM</div></div></div>
    <div class="topic"><svg class="topic-icon" viewBox="0 0 64 64"><use href="#chat"/></svg><div class="topic-main"><div class="topic-name">Achieve Goals</div><div class="topic-desc">Vivamus porttitor purus nisi eleifend libero a tempus libero</div></div><div class="topic-count">800<small>Posts</small></div><div class="topic-avatar" role="img" aria-label="Member avatar"></div><div class="topic-meta"><div class="latest">Pellentesque faucibus</div><div>By Author Name</div><div>Sunday at 11:28 AM</div></div></div>
    <div style="height:46px"></div>
  </div>
</section>

<section class="board" style="top:1481px">
  <div class="board-head">8 WEEK CHALLENGES <svg width="28" height="16"><use href="#chev"/></svg></div>
  <div class="board-body">
    <div class="topic"><svg class="topic-icon" viewBox="0 0 64 64"><use href="#chat"/></svg><div class="topic-main"><div class="topic-name">Fitness Training Questions</div><div class="topic-desc">Vivamus porttitor purus nisi eleifend libero a tempus libero</div></div><div class="topic-count">1200<small>Posts</small></div><div class="topic-avatar" role="img" aria-label="Member avatar"></div><div class="topic-meta"><div class="latest">Pellentesque faucibus</div><div>By Author Name</div><div>Sunday at 11:28 AM</div></div></div>
    <div class="topic"><svg class="topic-icon" viewBox="0 0 64 64"><use href="#chat"/></svg><div class="topic-main"><div class="topic-name">Weight Loss</div><div class="topic-desc">Vivamus porttitor purus nisi eleifend libero a tempus libero</div></div><div class="topic-count">525<small>Posts</small></div><div class="topic-avatar" role="img" aria-label="Member avatar"></div><div class="topic-meta"><div class="latest">Pellentesque faucibus</div><div>By Author Name</div><div>Sunday at 11:28 AM</div></div></div>
    <div class="topic"><svg class="topic-icon" viewBox="0 0 64 64"><use href="#chat"/></svg><div class="topic-main"><div class="topic-name">Achieve Goals</div><div class="topic-desc">Vivamus porttitor purus nisi eleifend libero a tempus libero</div></div><div class="topic-count">850<small>Posts</small></div><div class="topic-avatar" role="img" aria-label="Member avatar"></div><div class="topic-meta"><div class="latest">Pellentesque faucibus</div><div>By Author Name</div><div>Sunday at 11:28 AM</div></div></div>
    <div class="topic"><svg class="topic-icon" viewBox="0 0 64 64"><use href="#chat"/></svg><div class="topic-main"><div class="topic-name">Tracking Goals</div><div class="topic-desc">Vivamus porttitor purus nisi eleifend libero a tempus libero</div></div><div class="topic-count">750<small>Posts</small></div><div class="topic-avatar" role="img" aria-label="Member avatar"></div><div class="topic-meta"><div class="latest">Pellentesque faucibus</div><div>By Author Name</div><div>Sunday at 11:28 AM</div></div></div>
    <div style="height:35px"></div>
  </div>
</section>

<section class="board" style="top:1948px">
  <div class="board-head">LEVEL UP YOUR LIFE <svg width="28" height="16"><use href="#chev"/></svg></div>
  <div class="board-body">
    <div class="topic"><svg class="topic-icon" viewBox="0 0 64 64"><use href="#chat"/></svg><div class="topic-main"><div class="topic-name">Fitness Training Questions</div><div class="topic-desc">Vivamus porttitor purus nisi eleifend libero a tempus libero</div></div><div class="topic-count">1100<small>Posts</small></div><div class="topic-avatar" role="img" aria-label="Member avatar"></div><div class="topic-meta"><div class="latest">Pellentesque faucibus</div><div>By Author Name</div><div>Sunday at 11:28 AM</div></div></div>
    <div class="topic"><svg class="topic-icon" viewBox="0 0 64 64"><use href="#chat"/></svg><div class="topic-main"><div class="topic-name">Weight Loss</div><div class="topic-desc">Vivamus porttitor purus nisi eleifend libero a tempus libero</div></div><div class="topic-count">2200<small>Posts</small></div><div class="topic-avatar" role="img" aria-label="Member avatar"></div><div class="topic-meta"><div class="latest">Pellentesque faucibus</div><div>By Author Name</div><div>Sunday at 11:28 AM</div></div></div>
    <div style="height:31px"></div>
  </div>
</section>

<svg class="more" width="56" height="30" viewBox="0 0 56 30" aria-label="Show more"><polyline points="2,2 28,26 54,2" fill="none" stroke="#999" stroke-width="2"/></svg>

<aside class="ads">
  <div class="ad" role="img" aria-label="Advertisement: free town event poster" style="left:195px;width:231px;height:193px;background:linear-gradient(160deg,#f7a11a,#e8731b);border:2px solid #1a1a1a"></div>
  <div class="ad" role="img" aria-label="Advertisement: content discovery service" style="left:485px;width:231px;height:193px;background:linear-gradient(180deg,#3a3a3a,#222)"></div>
  <div class="ad" role="img" aria-label="Advertisement: environmental campaign over a prairie farm" style="left:764px;width:225px;height:188px;background:linear-gradient(180deg,#5d7d96 0%,#8fa8b8 45%,#9a8a3c 60%,#6e6a2a 100%)"></div>
</aside>

<footer class="site-footer">
  <div class="footer-brand">IRON SUMMIT</div>
  <nav class="footer-nav">
    <a href="#">ABOUT US</a><a href="#">FORUMS</a><a href="#">GOALS</a><a href="#">HEALTH</a><a href="#">WEALTH</a><a href="#">CONTACT</a>
  </nav>
  <p class="copyright">© 2019 Company Name  All right reserved</p>
  <div class="social"><span aria-label="Social link"></span><span aria-label="Social link"></span><span aria-label="Social link"></span></div>
</footer>
</body>
</html>
```